Movie Poster - Beneath The Amber Tide

Documentary-film poster design.
Attached is a PDF brief with information on what is required and examples of poster designs I like.

The project is a true crime / mystery documentary film. Set in the Soviet Union in 1959.

Colors
3276b5
85abd2
ec1f27

```html
<!DOCTYPE html>
<html lang="en">
<head>
<meta charset="utf-8">
<title>Beneath The Amber Tide – Documentary Film</title>
<link rel="stylesheet" href="https://fonts.googleapis.com/css2?family=Anton&family=Montserrat:wght@400;700&display=swap">
<style>
  :root {
    --ink: #0b0b0b;
    --night: #141414;
    --mist: #d9d9d9;
    --snow: #f7f7f7;
    --alert: #ec1f27;
    --steel: #3276b5;
    --frost: #85abd2;
  }
  html, body {
    margin: 0;
    padding: 0;
    overflow: hidden;
    background: var(--ink);
  }
  .poster {
    position: relative;
    width: 796px;
    height: 1200px;
    overflow: hidden;
    background: var(--night);
    font-family: "Montserrat", Arial, sans-serif;
  }
  .backdrop-photo {
    position: absolute;
    inset: 0;
    background:
      radial-gradient(ellipse 380px 330px at 250px 860px, rgba(255,255,255,1) 0%, rgba(246,248,250,0.92) 40%, rgba(160,172,184,0.4) 72%, rgba(0,0,0,0) 100%),
      radial-gradient(ellipse 460px 320px at 640px 760px, rgba(110,128,146,0.45) 0%, rgba(0,0,0,0) 100%),
      linear-gradient(180deg, #101010 0%, #181818 36%, #2c3036 56%, #5a5f66 72%, #2a2d31 100%);
  }
  .hikers-photo {
    position: absolute;
    left: 110px;
    top: 420px;
    width: 580px;
    height: 250px;
    background: radial-gradient(ellipse at 40% 55%, rgba(0,0,0,0.55) 0%, rgba(0,0,0,0) 70%);
  }
  .landscape-photo {
    position: absolute;
    left: 0;
    right: 0;
    bottom: 0;
    height: 200px;
    background:
      linear-gradient(180deg,
        rgba(30,36,44,0.9) 0%,
        rgba(40,48,58,0.95) 22%,
        rgba(196,208,220,0.95) 42%,
        rgba(232,238,244,0.95) 58%,
        rgba(120,134,150,0.95) 78%,
        rgba(22,26,32,1) 100%);
  }
  .landscape-photo::after {
    content: "";
    position: absolute;
    inset: 0;
    background: linear-gradient(90deg, rgba(10,12,16,0.75) 0%, rgba(10,12,16,0) 30%, rgba(10,12,16,0) 70%, rgba(10,12,16,0.7) 100%);
  }
  .teaser {
    position: absolute;
    top: 50px;
    left: 0;
    width: 800px;
    margin: 0;
    padding: 0;
    list-style: none;
    text-align: center;
    color: var(--mist);
    font-weight: 400;
    font-size: 14px;
    letter-spacing: 0.3px;
  }
  .teaser li { height: 41.3px; }
  .title {
    position: absolute;
    left: 0;
    top: 0;
  }
  .title text { font-family: "Anton", "Oswald", sans-serif; }
  .credit {
    position: absolute;
    top: 930px;
    left: 0;
    width: 820px;
    text-align: center;
    margin: 0;
    font-weight: 700;
    font-size: 14px;
    color: var(--ink);
    letter-spacing: 0.3px;
  }
  .tagline {
    position: absolute;
    top: 984px;
    left: 181px;
    margin: 0;
    font-weight: 700;
    font-size: 13.6px;
    color: var(--ink);
    white-space: nowrap;
    letter-spacing: 0.2px;
  }
  .tagline .highlight { color: var(--alert); }
</style>
</head>
<body>
<main class="poster">
  <div class="backdrop-photo" role="img" aria-label="Dark grainy winter photograph with light glowing at the lower left"></div>
  <div class="hikers-photo" role="img" aria-label="Silhouettes of hikers with backpacks and ski poles"></div>
  <div class="landscape-photo" role="img" aria-label="Black and white photograph of a snowy valley with wooden cabins, a pine treeline and bare trees"></div>

  <ul class="teaser">
    <li>THE FILM</li>
    <li>IS ABOUT</li>
    <li>THE VETROV PASS</li>
    <li>INCIDENT</li>
    <li>THAT HAPPENED</li>
    <li>IN RUSSIA</li>
    <li>IN</li>
    <li>1959.</li>
  </ul>

  <svg class="title" width="796" height="1200" viewBox="0 0 796 1200" role="img" aria-label="Beneath The Amber Tide">
    <defs>
      <linearGradient id="snow-fill" x1="0" y1="0" x2="0" y2="1">
        <stop offset="0" stop-color="#f4f6f8"/>
        <stop offset="0.5" stop-color="#aebfd0"/>
        <stop offset="1" stop-color="#e8edf2"/>
      </linearGradient>
      <linearGradient id="frost-fill" x1="0" y1="0" x2="1" y2="1">
        <stop offset="0" stop-color="#f7f7f7"/>
        <stop offset="0.55" stop-color="#85abd2"/>
        <stop offset="1" stop-color="#3276b5"/>
      </linearGradient>
      <linearGradient id="blood-fill" x1="0" y1="0" x2="0" y2="1">
        <stop offset="0" stop-color="#d0111a"/>
        <stop offset="1" stop-color="#9a0a0f"/>
      </linearGradient>
    </defs>
    <text x="89" y="595" font-size="183" fill="url(#blood-fill)" textLength="619" lengthAdjust="spacingAndGlyphs">BENEATH</text>
    <text x="28" y="757" font-size="183" fill="url(#snow-fill)" textLength="742" lengthAdjust="spacingAndGlyphs">THE AMBER</text>
    <text x="213" y="919" font-size="183" fill="url(#frost-fill)" textLength="372" lengthAdjust="spacingAndGlyphs">TIDE</text>
  </svg>

  <p class="credit">DOCUMENTARY FILM</p>
  <p class="tagline">NINE PEOPLE <span class="highlight">DIED</span> IN THE NORTHERN URAL MOUNTAINS</p>
</main>
</body>
</html>
```